PowerPoint Template for Meridian Liaison Hub. Website is www.meridianliaisonhub.example

The tagline for the Center is "Connecting the brightest minds in healthcare"

```html
<!DOCTYPE html>
<html lang="en">
<head>
<meta charset="utf-8">
<title>Meridian Liaison Hub — Presentation Template</title>
<link href="https://fonts.googleapis.com/css2?family=Montserrat:wght@300;400;600;700&family=Open+Sans:wght@400;600&display=swap" rel="stylesheet">
<style>
:root{
  --navy:#1d4f86;
  --blue:#2a74c9;
  --sky:#4a98e6;
  --ink:#3b3f44;
  --grey:#6b7075;
  --slate:#4a4d51;
  --mist:#eceff2;
  --line:#d6dade;
  --paper:#ffffff;
  --photo-a:#d3e0ec;
  --photo-b:#8ea8c1;
}
*{box-sizing:border-box;margin:0;padding:0}
html,body{width:1200px;height:4800px;overflow:hidden;background:var(--paper)}
body{font-family:"Open Sans",Arial,sans-serif;color:var(--ink)}
.deck{display:grid;grid-template-columns:repeat(3,396px);grid-template-rows:repeat(21,223px);column-gap:6px;row-gap:5px;padding-top:8px}
.slide{position:relative;overflow:hidden;background:var(--paper);outline:1px solid #e2e5e8}
.a{position:absolute}
.s-title{position:absolute;left:14px;top:11px;font-family:"Montserrat",Arial,sans-serif;font-weight:400;font-size:12px;letter-spacing:.6px;text-transform:uppercase;color:var(--navy)}
.s-title::after{content:"";display:block;width:26px;height:2px;background:var(--blue);margin-top:3px}
.foot{position:absolute;left:0;right:0;bottom:0;height:14px;border-top:1px solid var(--line);display:flex;align-items:center;padding:0 10px;gap:4px;font-family:"Montserrat",Arial,sans-serif;font-size:5px;color:var(--grey);background:var(--paper)}
.foot .mk{width:6px;height:6px;border-radius:50%;background:var(--blue)}
.foot b{color:var(--navy);font-weight:700;letter-spacing:.4px}
.foot em{font-style:normal;flex:1;text-align:center}
.foot i{font-style:normal;background:var(--blue);color:#fff;padding:1px 4px}
.ph{background:linear-gradient(135deg,var(--photo-a),var(--photo-b))}
.ph.dark{background:linear-gradient(135deg,#7f8c99,#3e4a57)}
.ph.teal{background:linear-gradient(135deg,#b7dccf,#3e8d86)}
.ph.warm{background:linear-gradient(135deg,#e3e6ea,#a9b6c3)}
.t{font-size:5px;line-height:1.45;color:var(--grey)}
.t.w{color:#fff}
.h{font-family:"Montserrat",Arial,sans-serif;font-size:7px;font-weight:600;color:var(--ink)}
.h.w{color:#fff}
.h.b{color:var(--blue)}
.big{font-family:"Montserrat",Arial,sans-serif;font-weight:300;color:#fff}
.num{font-family:"Montserrat",Arial,sans-serif;font-weight:300;color:var(--blue)}
.bg-navy{background:var(--navy)}
.bg-blue{background:var(--blue)}
.bg-sky{background:var(--sky)}
.bg-grey{background:var(--grey)}
.bg-slate{background:var(--slate)}
.bg-mist{background:var(--mist)}
.dot{border-radius:50%}
.brand{font-family:"Montserrat",Arial,sans-serif;font-weight:700;font-size:9px;letter-spacing:.6px;color:#fff;display:flex;align-items:center;gap:4px}
.brand .c{width:10px;height:10px;border-radius:50%;background:#fff}
.client{display:flex;align-items:center;justify-content:center;font-family:"Montserrat",Arial,sans-serif;font-weight:600;font-size:8px;color:var(--navy);border:1px solid var(--line);background:#fff}
.row-item{display:flex;gap:5px;align-items:flex-start}
.ic{width:12px;height:12px;border-radius:50%;background:var(--blue);flex:none}
.ic.sq{border-radius:2px}
.bar{position:absolute;bottom:0}
table.data{border-collapse:collapse;font-size:5px;color:var(--grey)}
table.data th{background:var(--slate);color:#fff;font-weight:600;padding:2px 6px;text-align:left}
table.data td{padding:2px 6px;border-bottom:1px solid var(--line)}
table.data tr:nth-child(odd) td{background:var(--mist)}
</style>
</head>
<body>
<main class="deck">

<!-- Row 1: title slides -->
<section class="slide">
  <div class="a ph" style="inset:0" role="img" aria-label="Photo of a medical team in a bright clinic"></div>
  <div class="a bg-navy" style="left:0;top:0;width:230px;height:223px;opacity:.92"></div>
  <div class="a brand" style="left:16px;top:18px"><span class="c"></span>MERIDIAN LIAISON HUB</div>
  <div class="a big" style="left:16px;top:95px;font-size:19px">YOUR TITLE GOES HERE</div>
  <div class="a t w" style="left:16px;top:122px;width:190px">Connecting the brightest minds in healthcare</div>
</section>
<section class="slide">
  <div class="a ph dark" style="inset:0" role="img" aria-label="Muted photo of doctors at work"></div>
  <div class="a big" style="left:0;right:0;top:92px;text-align:center;font-size:19px">YOUR TITLE GOES HERE</div>
  <div class="a t w" style="left:0;right:0;top:118px;text-align:center">Connecting the brightest minds in healthcare</div>
</section>
<section class="slide">
  <div class="a ph" style="inset:0" role="img" aria-label="Photo of a smiling physician"></div>
  <div class="a bg-blue" style="left:0;top:0;width:396px;height:223px;opacity:.78"></div>
  <div class="a brand" style="left:120px;top:16px"><span class="c"></span>MERIDIAN LIAISON HUB</div>
  <div class="a big" style="left:20px;top:92px;font-size:19px">YOUR TITLE GOES HERE</div>
  <div class="a t w" style="left:20px;top:118px">Connecting the brightest minds in healthcare</div>
</section>

<!-- Row 2: about us -->
<section class="slide bg-navy">
  <div class="s-title" style="color:#fff">About Us</div>
  <p class="a t w" style="left:14px;top:40px;width:368px">Our liaison teams link clinics, labs and regional partners so patients receive faster, clearer and better coordinated care every day. We bring specialists, nurses and planners together around one shared record, one shared schedule and one shared goal. Each office reports weekly on referrals, waiting times and outcomes, and every lesson learned is shared across the network.</p>
  <footer class="foot"><span class="mk"></span><b>MERIDIAN</b><em>Connecting the brightest minds in healthcare</em><i>04</i></footer>
</section>
<section class="slide">
  <div class="s-title">About Us</div>
  <p class="a t" style="left:14px;top:40px;width:250px">Our liaison teams link clinics, labs and regional partners so patients receive faster, clearer and better coordinated care every day. We bring specialists, nurses and planners together around one shared record and one shared goal.</p>
  <footer class="foot"><span class="mk"></span><b>MERIDIAN</b><em>Connecting the brightest minds in healthcare</em><i>05</i></footer>
</section>
<section class="slide bg-slate">
  <div class="a brand" style="left:14px;top:14px"><span class="c"></span>MERIDIAN</div>
  <div class="a h w" style="left:14px;top:40px">ABOUT US</div>
  <p class="a t w" style="left:14px;top:54px;width:250px">We bring specialists, nurses and planners together around one shared record, one shared schedule and one shared goal for every patient.</p>
  <footer class="foot"><span class="mk"></span><b>MERIDIAN</b><em>Connecting the brightest minds in healthcare</em><i>06</i></footer>
</section>

<!-- Row 3 -->
<section class="slide">
  <div class="s-title">Our Agenda</div>
  <div class="a" style="left:14px;top:44px;width:120px;display:grid;gap:10px">
    <div class="row-item"><span class="ic sq"></span><div><div class="h">Heading Here</div><div class="t">Short summary of the topic.</div></div></div>
    <div class="row-item"><span class="ic sq"></span><div><div class="h">Heading Here</div><div class="t">Short summary of the topic.</div></div></div>
    <div class="row-item"><span class="ic sq"></span><div><div class="h">Heading Here</div><div class="t">Short summary of the topic.</div></div></div>
  </div>
  <div class="a" style="left:210px;top:44px;width:170px;display:grid;grid-template-columns:1fr 1fr;gap:14px 10px">
    <div class="row-item"><span class="ic sq"></span><div class="h">Heading Here</div></div>
    <div class="row-item"><span class="ic sq"></span><div class="h">Heading Here</div></div>
    <div class="row-item"><span class="ic sq"></span><div class="h">Heading Here</div></div>
    <div class="row-item"><span class="ic sq"></span><div class="h">Heading Here</div></div>
  </div>
  <footer class="foot"><span class="mk"></span><b>MERIDIAN</b><em>Connecting the brightest minds in healthcare</em><i>07</i></footer>
</section>
<section class="slide">
  <div class="s-title">Market Overview</div>
  <div class="a ph" style="left:14px;top:42px;width:120px;height:80px" role="img" aria-label="Photo of three doctors standing together"></div>
  <svg class="a" style="left:150px;top:42px" width="80" height="80" viewBox="0 0 80 80"><circle cx="40" cy="40" r="30" fill="none" stroke="#eceff2" stroke-width="10"/><circle cx="40" cy="40" r="30" fill="none" stroke="#2a74c9" stroke-width="10" stroke-dasharray="113 189" transform="rotate(-90 40 40)"/><text x="40" y="44" text-anchor="middle" font-family="Montserrat" font-size="11" fill="#1d4f86">60%</text></svg>
  <div class="a bg-navy" style="left:250px;top:42px;width:132px;height:80px;padding:8px"><div class="h w">Heading Here</div><p class="t w">Referrals routed through our hub grew steadily this year.</p></div>
  <p class="a t" style="left:14px;top:135px;width:368px">Regional demand for coordinated specialist care continues to rise across every partner clinic we serve.</p>
  <footer class="foot"><span class="mk"></span><b>MERIDIAN</b><em>Connecting the brightest minds in healthcare</em><i>08</i></footer>
</section>
<section class="slide">
  <div class="s-title">Bullets Point Level</div>
  <div class="a" style="left:14px;top:48px;width:368px;display:grid;grid-template-columns:1fr 1fr;gap:18px 20px">
    <div class="row-item"><span class="ic"></span><div><div class="h">Your Heading</div><div class="t">Brief line about this point.</div></div></div>
    <div class="row-item"><span class="ic"></span><div><div class="h">Your Heading</div><div class="t">Brief line about this point.</div></div></div>
    <div class="row-item"><span class="ic"></span><div><div class="h">Your Heading</div><div class="t">Brief line about this point.</div></div></div>
    <div class="row-item"><span class="ic"></span><div><div class="h">Your Heading</div><div class="t">Brief line about this point.</div></div></div>
    <div class="row-item"><span class="ic"></span><div><div class="h">Your Heading</div><div class="t">Brief line about this point.</div></div></div>
    <div class="row-item"><span class="ic"></span><div><div class="h">Your Heading</div><div class="t">Brief line about this point.</div></div></div>
  </div>
  <footer class="foot"><span class="mk"></span><b>MERIDIAN</b><em>Connecting the brightest minds in healthcare</em><i>09</i></footer>
</section>

<!-- Row 4 -->
<section class="slide">
  <div class="a ph" style="left:0;top:0;width:130px;height:100px" role="img" aria-label="Photo of a nurse with a patient"></div>
  <div class="a ph warm" style="left:130px;top:0;width:130px;height:100px" role="img" aria-label="Photo of a doctor in a corridor"></div>
  <div class="a ph" style="left:260px;top:0;width:136px;height:209px" role="img" aria-label="Photo of a care team meeting"></div>
  <div class="a ph warm" style="left:0;top:100px;width:130px;height:109px" role="img" aria-label="Photo of a clinician outdoors"></div>
  <div class="a bg-slate" style="left:130px;top:100px;width:130px;height:109px;padding:12px"><div class="h w">Your Title</div><p class="t w">Teams that share one plan deliver calmer, safer visits.</p></div>
  <footer class="foot"><span class="mk"></span><b>MERIDIAN</b><em>Connecting the brightest minds in healthcare</em><i>10</i></footer>
</section>
<section class="slide">
  <div class="s-title">Your Title Here</div>
  <div class="a bg-navy" style="left:14px;top:40px;width:88px;height:150px;padding:8px"><div class="h w">Heading Here</div><p class="t w">Short note on this service area.</p></div>
  <div class="a ph" style="left:104px;top:40px;width:88px;height:150px" role="img" aria-label="Photo of a doctor"></div>
  <div class="a bg-blue" style="left:194px;top:40px;width:88px;height:150px;padding:8px"><div class="h w">Heading Here</div><p class="t w">Short note on this service area.</p></div>
  <div class="a bg-slate" style="left:284px;top:40px;width:98px;height:150px;padding:8px"><div class="h w">Heading Here</div><p class="t w">Short note on this service area.</p></div>
  <footer class="foot"><span class="mk"></span><b>MERIDIAN</b><em>Connecting the brightest minds in healthcare</em><i>11</i></footer>
</section>
<section class="slide">
  <div class="s-title">Our Differences</div>
  <div class="a" style="left:14px;top:44px;width:200px;display:grid;gap:12px">
    <div class="row-item"><span class="ic"></span><div class="t">One shared record for every referral.</div></div>
    <div class="row-item"><span class="ic"></span><div class="t">Specialists reachable within one working day.</div></div>
    <div class="row-item"><span class="ic"></span><div class="t">Clear weekly reports for each partner.</div></div>
    <div class="row-item"><span class="ic"></span><div class="t">Local staff who know the region well.</div></div>
  </div>
  <div class="a ph" style="left:232px;top:44px;width:150px;height:140px" role="img" aria-label="Photo of doctors reviewing notes"></div>
  <footer class="foot"><span class="mk"></span><b>MERIDIAN</b><em>Connecting the brightest minds in healthcare</em><i>12</i></footer>
</section>

<!-- Row 5 -->
<section class="slide">
  <div class="s-title">Text &amp; Bullet Area</div>
  <p class="a t" style="left:14px;top:48px;width:150px">Our liaison teams link clinics, labs and regional partners so patients receive faster, clearer care.</p>
  <div class="a" style="left:200px;top:44px;width:180px;display:grid;gap:11px">
    <div class="row-item"><span class="ic" style="background:var(--grey)"></span><div class="t">Heading here with a short line.</div></div>
    <div class="row-item"><span class="ic" style="background:var(--grey)"></span><div class="t">Heading here with a short line.</div></div>
    <div class="row-item"><span class="ic" style="background:var(--grey)"></span><div class="t">Heading here with a short line.</div></div>
    <div class="row-item"><span class="ic" style="background:var(--grey)"></span><div class="t">Heading here with a short line.</div></div>
  </div>
  <footer class="foot"><span class="mk"></span><b>MERIDIAN</b><em>Connecting the brightest minds in healthcare</em><i>13</i></footer>
</section>
<section class="slide">
  <div class="a client" style="left:14px;top:18px;width:110px;height:40px">Northfield</div>
  <div class="a client" style="left:143px;top:18px;width:110px;height:40px">Lumen Studio</div>
  <div class="a client" style="left:272px;top:18px;width:110px;height:40px">Harbor Lane</div>
  <div class="a client" style="left:14px;top:75px;width:110px;height:40px">Oakridge</div>
  <div class="a bg-navy" style="left:143px;top:70px;width:110px;height:60px;display:flex;align-items:center;justify-content:center;font-family:Montserrat,Arial,sans-serif;font-size:11px;color:#fff;text-align:center">Our Awesome Client</div>
  <div class="a client" style="left:272px;top:75px;width:110px;height:40px">Clearwater</div>
  <div class="a client" style="left:14px;top:140px;width:110px;height:40px">Silverpine</div>
  <div class="a client" style="left:143px;top:140px;width:110px;height:40px">Brightmoor</div>
  <div class="a client" style="left:272px;top:140px;width:110px;height:40px">Westvale</div>
  <footer class="foot"><span class="mk"></span><b>MERIDIAN</b><em>Connecting the brightest minds in healthcare</em><i>14</i></footer>
</section>
<section class="slide">
  <div class="a" style="left:0;top:0;width:396px;height:209px;display:grid;grid-template-columns:repeat(5,1fr)">
    <div style="background:#f2f4f6;padding:60px 8px 0;text-align:center"><span class="ic" style="display:inline-block;background:var(--grey)"></span><div class="h">Heading Here</div><p class="t">Short line of text.</p></div>
    <div style="background:#e3e6e9;padding:60px 8px 0;text-align:center"><span class="ic" style="display:inline-block;background:var(--grey)"></span><div class="h">Heading Here</div><p class="t">Short line of text.</p></div>
    <div style="background:#c9ced3;padding:60px 8px 0;text-align:center"><span class="ic" style="display:inline-block;background:#fff"></span><div class="h">Heading Here</div><p class="t">Short line of text.</p></div>
    <div style="background:var(--grey);padding:60px 8px 0;text-align:center"><span class="ic" style="display:inline-block;background:#fff"></span><div class="h w">Heading Here</div><p class="t w">Short line of text.</p></div>
    <div style="background:var(--navy);padding:60px 8px 0;text-align:center"><span class="ic" style="display:inline-block;background:#fff"></span><div class="h w">Heading Here</div><p class="t w">Short line of text.</p></div>
  </div>
  <footer class="foot"><span class="mk"></span><b>MERIDIAN</b><em>Connecting the brightest minds in healthcare</em><i>15</i></footer>
</section>

<!-- Row 6 -->
<section class="slide">
  <div class="s-title">Our Mockup Area</div>
  <div class="a" style="left:14px;top:40px;width:210px;height:132px;background:#2f3337;padding:6px;border-radius:4px 4px 0 0"><div class="ph" style="width:100%;height:100%" role="img" aria-label="Screen showing a photo of three doctors"></div></div>
  <div class="a" style="left:4px;top:172px;width:230px;height:6px;background:#b9bec3;border-radius:0 0 4px 4px"></div>
  <div class="a bg-slate" style="left:250px;top:40px;width:132px;height:140px;padding:10px"><div class="h w">Heading Here</div><p class="t w">A simple portal that lets partner clinics book specialists and follow each referral.</p></div>
  <footer class="foot"><span class="mk"></span><b>MERIDIAN</b><em>Connecting the brightest minds in healthcare</em><i>16</i></footer>
</section>
<section class="slide">
  <div class="a bg-navy" style="left:0;top:0;width:130px;height:209px"></div>
  <div class="a dot" style="left:25px;top:60px;width:80px;height:80px;border:2px solid #fff;display:flex;align-items:center;justify-content:center;text-align:center;font-family:Montserrat,Arial,sans-serif;font-size:9px;color:#fff">PICTURE<br>SLIDE</div>
  <div class="a" style="left:160px;top:30px;width:210px;height:100px;border-bottom:1px solid var(--line)">
    <div class="bar bg-navy" style="left:10px;width:16px;height:45px"></div>
    <div class="bar bg-blue" style="left:40px;width:16px;height:70px"></div>
    <div class="bar bg-navy" style="left:70px;width:16px;height:55px"></div>
    <div class="bar bg-blue" style="left:100px;width:16px;height:85px"></div>
    <div class="bar bg-navy" style="left:130px;width:16px;height:60px"></div>
    <div class="bar bg-blue" style="left:160px;width:16px;height:92px"></div>
  </div>
  <div class="a num" style="left:160px;top:145px;font-size:20px">85%</div>
  <p class="a t" style="left:225px;top:150px;width:150px">Share of referrals closed within one week.</p>
  <footer class="foot"><span class="mk"></span><b>MERIDIAN</b><em>Connecting the brightest minds in healthcare</em><i>17</i></footer>
</section>
<section class="slide">
  <div class="s-title">Our Mockup Area</div>
  <div class="a" style="left:14px;top:48px;width:150px"><div class="h">Heading Here</div><p class="t">Partner clinics see live availability and book specialists in minutes.</p></div>
  <div class="a" style="left:180px;top:40px;width:200px;height:125px;background:#2f3337;padding:6px;border-radius:3px"><div class="ph" style="width:100%;height:100%" role="img" aria-label="Screen showing a photo of a doctor and patient"></div></div>
  <div class="a" style="left:265px;top:165px;width:30px;height:12px;background:#b9bec3"></div>
  <footer class="foot"><span class="mk"></span><b>MERIDIAN</b><em>Connecting the brightest minds in healthcare</em><i>18</i></footer>
</section>

<!-- Row 7 -->
<section class="slide">
  <div class="s-title">Your Blank Slide</div>
  <footer class="foot"><span class="mk"></span><b>MERIDIAN</b><em>Connecting the brightest minds in healthcare</em><i>19</i></footer>
</section>
<section class="slide">
  <div class="s-title">Your Title Goes Here</div>
  <div class="a" style="left:80px;top:40px;width:236px;height:150px;display:grid;grid-template-columns:1fr 1fr;grid-template-rows:1fr 1fr;gap:3px">
    <div class="ph dark" role="img" aria-label="Photo of a hospital hallway"></div>
    <div class="bg-navy" style="padding:10px"><div class="h w">Heading Here</div></div>
    <div class="bg-navy" style="padding:10px"><div class="h w">Heading Here</div></div>
    <div class="ph dark" role="img" aria-label="Photo of medical equipment"></div>
  </div>
  <footer class="foot"><span class="mk"></span><b>MERIDIAN</b><em>Connecting the brightest minds in healthcare</em><i>20</i></footer>
</section>
<section class="slide">
  <div class="a ph teal" style="left:0;top:0;width:396px;height:209px" role="img" aria-label="Microscope image of cells in green tones"></div>
  <div class="a bg-navy" style="left:250px;top:50px;width:120px;height:110px;padding:12px;opacity:.94"><div class="h w">About Us</div><p class="t w">We connect clinics and specialists across the region.</p></div>
  <footer class="foot"><span class="mk"></span><b>MERIDIAN</b><em>Connecting the brightest minds in healthcare</em><i>21</i></footer>
</section>

<!-- Row 8 -->
<section class="slide">
  <div class="a ph warm" style="inset:0" role="img" aria-label="Soft grey photo of a physician"></div>
  <div class="a" style="inset:0;background:rgba(110,116,122,.7)"></div>
  <div class="a big" style="left:16px;top:150px;font-size:15px">THIS IS YOUR DIVIDER PAGE</div>
  <div class="a t w" style="left:16px;top:172px">Section subtitle here</div>
</section>
<section class="slide">
  <div class="s-title">Quote Area</div>
  <div class="a bg-navy" style="left:14px;top:45px;width:170px;height:130px;padding:14px"><p class="t w" style="font-size:6px">“Coming together is a beginning, keeping together is progress, working together is success.”</p><div class="h w" style="margin-top:10px">— Alden Marsh</div></div>
  <div class="a ph" style="left:190px;top:45px;width:192px;height:130px" role="img" aria-label="Photo of a doctor consulting a patient"></div>
  <footer class="foot"><span class="mk"></span><b>MERIDIAN</b><em>Connecting the brightest minds in healthcare</em><i>22</i></footer>
</section>
<section class="slide">
  <div class="s-title">Brand Detailed</div>
  <div class="a ph" style="left:14px;top:40px;width:170px;height:150px" role="img" aria-label="Photo of clinicians in a bright room"></div>
  <div class="a" style="left:196px;top:40px;width:186px;height:150px;display:grid;grid-template-columns:1fr 1fr;gap:4px">
    <div class="bg-navy" style="padding:8px"><div class="h w">Heading</div><p class="t w">Short line here.</p></div>
    <div class="bg-blue" style="padding:8px"><div class="h w">Heading</div><p class="t w">Short line here.</p></div>
    <div class="bg-grey" style="padding:8px"><div class="h w">Heading</div><p class="t w">Short line here.</p></div>
    <div class="bg-mist" style="padding:8px"><div class="h">Heading</div><p class="t">Short line here.</p></div>
  </div>
  <footer class="foot"><span class="mk"></span><b>MERIDIAN</b><em>Connecting the brightest minds in healthcare</em><i>23</i></footer>
</section>

<!-- Row 9 -->
<section class="slide">
  <div class="s-title">Product Philosophy</div>
  <svg class="a" style="left:148px;top:44px" width="100" height="100" viewBox="0 0 100 100"><circle cx="50" cy="50" r="36" fill="none" stroke="#1d4f86" stroke-width="18" stroke-dasharray="60 226" transform="rotate(-90 50 50)"/><circle cx="50" cy="50" r="36" fill="none" stroke="#2a74c9" stroke-width="18" stroke-dasharray="55 226" stroke-dashoffset="-60" transform="rotate(-90 50 50)"/><circle cx="50" cy="50" r="36" fill="none" stroke="#6b7075" stroke-width="18" stroke-dasharray="55 226" stroke-dashoffset="-115" transform="rotate(-90 50 50)"/><circle cx="50" cy="50" r="36" fill="none" stroke="#4a98e6" stroke-width="18" stroke-dasharray="56 226" stroke-dashoffset="-170" transform="rotate(-90 50 50)"/></svg>
  <div class="a" style="left:14px;top:55px;width:120px"><div class="h b">Heading Here</div><p class="t">Short line of text.</p></div>
  <div class="a" style="left:14px;top:115px;width:120px"><div class="h b">Heading Here</div><p class="t">Short line of text.</p></div>
  <div class="a" style="left:270px;top:55px;width:120px"><div class="h b">Heading Here</div><p class="t">Short line of text.</p></div>
  <div class="a" style="left:270px;top:115px;width:120px"><div class="h b">Heading Here</div><p class="t">Short line of text.</p></div>
  <footer class="foot"><span class="mk"></span><b>MERIDIAN</b><em>Connecting the brightest minds in healthcare</em><i>24</i></footer>
</section>
<section class="slide">
  <div class="a ph warm" style="left:0;top:0;width:396px;height:80px;opacity:.6" role="img" aria-label="Faded photo of a city skyline"></div>
  <div class="a" style="left:30px;top:30px;width:336px;height:120px;border-bottom:1px solid var(--line)">
    <div class="bar bg-navy" style="left:10px;width:26px;height:60px"></div><div class="bar bg-mist" style="left:38px;width:26px;height:40px"></div>
    <div class="bar bg-navy" style="left:80px;width:26px;height:80px"></div><div class="bar bg-mist" style="left:108px;width:26px;height:50px"></div>
    <div class="bar bg-blue" style="left:150px;width:26px;height:110px"></div><div class="bar bg-mist" style="left:178px;width:26px;height:70px"></div>
    <div class="bar bg-navy" style="left:220px;width:26px;height:70px"></div><div class="bar bg-mist" style="left:248px;width:26px;height:45px"></div>
    <div class="bar bg-navy" style="left:290px;width:26px;height:55px"></div>
  </div>
  <div class="a" style="left:30px;top:158px;width:336px;display:grid;grid-template-columns:repeat(4,1fr);text-align:center"><div class="h">Heading</div><div class="h">Heading</div><div class="h">Heading</div><div class="h">Heading</div></div>
  <footer class="foot"><span class="mk"></span><b>MERIDIAN</b><em>Connecting the brightest minds in healthcare</em><i>25</i></footer>
</section>
<section class="slide">
  <div class="s-title">Trending In The World</div>
  <div class="a" style="left:60px;top:40px;width:270px;height:130px;background:linear-gradient(135deg,#e9edf1,#c8d0d8)" role="img" aria-label="World map in light grey"></div>
  <div class="a num" style="left:70px;top:175px;font-size:11px">32%</div>
  <div class="a num" style="left:175px;top:175px;font-size:11px">48%</div>
  <div class="a num" style="left:280px;top:175px;font-size:11px">20%</div>
  <footer class="foot"><span class="mk"></span><b>MERIDIAN</b><em>Connecting the brightest minds in healthcare</em><i>26</i></footer>
</section>

<!-- Row 10 -->
<section class="slide">
  <div class="s-title">USA Map</div>
  <div class="a" style="left:14px;top:45px;width:190px;height:120px;background:linear-gradient(135deg,#8d949b,#3a3f44)" role="img" aria-label="Map of the United States with highlighted states"></div>
  <div class="a" style="left:225px;top:70px"><div class="h">Position Analysis</div><div class="num" style="font-size:24px">89%</div><p class="t" style="width:150px">Coverage of partner regions this year.</p></div>
  <div class="a" style="left:14px;top:178px;width:368px;height:6px;display:grid;grid-template-columns:repeat(5,1fr);gap:3px"><span class="bg-navy"></span><span class="bg-blue"></span><span class="bg-sky"></span><span class="bg-grey"></span><span class="bg-slate"></span></div>
  <footer class="foot"><span class="mk"></span><b>MERIDIAN</b><em>Connecting the brightest minds in healthcare</em><i>27</i></footer>
</section>
<section class="slide bg-navy">
  <div class="s-title" style="color:#fff">Our Vision &amp; Mission</div>
  <div class="a" style="left:14px;top:55px;width:170px"><div class="h w" style="font-size:9px">Our Vision</div><p class="t w">Every patient in the region reaches the right specialist without delay.</p></div>
  <div class="a" style="left:210px;top:55px;width:170px"><div class="h w" style="font-size:9px">Our Mission</div><p class="t w">Link clinics, labs and partners through one calm, shared process.</p></div>
  <footer class="foot"><span class="mk"></span><b>MERIDIAN</b><em>Connecting the brightest minds in healthcare</em><i>28</i></footer>
</section>
<section class="slide">
  <div class="s-title">Our Services</div>
  <div class="a ph" style="left:14px;top:42px;width:150px;height:140px" role="img" aria-label="Photo of a doctor with a patient"></div>
  <div class="a" style="left:180px;top:46px;width:200px;display:grid;gap:12px">
    <div class="row-item"><span class="ic"></span><div><div class="h">Service Here</div><div class="t">Short line about it.</div></div></div>
    <div class="row-item"><span class="ic"></span><div><div class="h">Service Here</div><div class="t">Short line about it.</div></div></div>
    <div class="row-item"><span class="ic"></span><div><div class="h">Service Here</div><div class="t">Short line about it.</div></div></div>
    <div class="row-item"><span class="ic"></span><div><div class="h">Service Here</div><div class="t">Short line about it.</div></div></div>
  </div>
  <footer class="foot"><span class="mk"></span><b>MERIDIAN</b><em>Connecting the brightest minds in healthcare</em><i>29</i></footer>
</section>

<!-- Row 11 -->
<section class="slide">
  <div class="s-title">Three Column Description</div>
  <p class="a t" style="left:14px;top:45px;width:110px">This is a place for your header text. Add a short intro for the three columns.</p>
  <div class="a" style="left:140px;top:45px;width:242px;display:grid;grid-template-columns:repeat(3,1fr);gap:10px">
    <div><div class="h b">Heading</div><p class="t">Short text about this column topic.</p></div>
    <div><div class="h b">Heading</div><p class="t">Short text about this column topic.</p></div>
    <div><div class="h b">Heading</div><p class="t">Short text about this column topic.</p></div>
  </div>
  <footer class="foot"><span class="mk"></span><b>MERIDIAN</b><em>Connecting the brightest minds in healthcare</em><i>30</i></footer>
</section>
<section class="slide">
  <div class="s-title">Our Team</div>
  <div class="a" style="left:30px;top:70px;width:120px"><div class="h">Team Member</div><p class="t">Lead liaison for northern clinics.</p></div>
  <div class="a dot ph" style="left:165px;top:45px;width:66px;height:66px" role="img" aria-label="Portrait photo of a team member"></div>
  <div class="a h" style="left:0;right:0;top:118px;text-align:center">Name Surname</div>
  <div class="a" style="left:172px;top:134px;display:flex;gap:5px"><span class="dot bg-navy" style="width:8px;height:8px"></span><span class="dot bg-navy" style="width:8px;height:8px"></span><span class="dot bg-navy" style="width:8px;height:8px"></span><span class="dot bg-navy" style="width:8px;height:8px"></span></div>
  <div class="a" style="left:250px;top:70px;width:120px"><div class="h">Team Member</div><p class="t">Coordinator for lab partners.</p></div>
  <footer class="foot"><span class="mk"></span><b>MERIDIAN</b><em>Connecting the brightest minds in healthcare</em><i>31</i></footer>
</section>
<section class="slide">
  <div class="s-title">Monthly Subscription</div>
  <div class="a" style="left:50px;top:45px;width:296px;height:140px;display:grid;grid-template-columns:repeat(3,1fr);gap:4px;text-align:center">
    <div class="bg-mist"><div class="bg-grey" style="padding:8px;font-family:Montserrat,Arial,sans-serif;color:#fff;font-size:12px">$300</div><p class="t" style="padding:8px">Basic plan<br>One clinic<br>Email support</p></div>
    <div class="bg-mist"><div class="bg-slate" style="padding:8px;font-family:Montserrat,Arial,sans-serif;color:#fff;font-size:12px">$500</div><p class="t" style="padding:8px">Full plan<br>Five clinics<br>Phone support</p></div>
    <div class="bg-mist"><div class="bg-navy" style="padding:8px;font-family:Montserrat,Arial,sans-serif;color:#fff;font-size:12px">$400</div><p class="t" style="padding:8px">Plus plan<br>Three clinics<br>Chat support</p></div>
  </div>
  <footer class="foot"><span class="mk"></span><b>MERIDIAN</b><em>Connecting the brightest minds in healthcare</em><i>32</i></footer>
</section>

<!-- Row 12 -->
<section class="slide">
  <div class="s-title">Your Title Goes Here</div>
  <table class="data a" style="left:14px;top:42px;width:368px">
    <tr><th>Region</th><th>Clinics</th><th>Referrals</th><th>Growth</th></tr>
    <tr><td>North</td><td>12</td><td>340</td><td>8%</td></tr>
    <tr><td>South</td><td>9</td><td>280</td><td>6%</td></tr>
    <tr><td>East</td><td>14</td><td>410</td><td>11%</td></tr>
    <tr><td>West</td><td>7</td><td>190</td><td>4%</td></tr>
    <tr><td>Central</td><td>10</td><td>305</td><td>9%</td></tr>
  </table>
  <footer class="foot"><span class="mk"></span><b>MERIDIAN</b><em>Connecting the brightest minds in healthcare</em><i>33</i></footer>
</section>
<section class="slide">
  <div class="s-title">Our Team</div>
  <div class="a" style="left:14px;top:45px;width:368px;display:grid;grid-template-columns:1fr 1fr;gap:14px 20px">
    <div class="row-item"><div class="ph" style="width:38px;height:38px;flex:none" role="img" aria-label="Portrait photo of a team member"></div><div><div class="h">Name Surname</div><div class="t">Position here</div></div></div>
    <div class="row-item"><div class="ph" style="width:38px;height:38px;flex:none" role="img" aria-label="Portrait photo of a team member"></div><div><div class="h">Name Surname</div><div class="t">Position here</div></div></div>
    <div class="row-item"><div class="ph" style="width:38px;height:38px;flex:none" role="img" aria-label="Portrait photo of a team member"></div><div><div class="h">Name Surname</div><div class="t">Position here</div></div></div>
    <div class="row-item"><div class="ph" style="width:38px;height:38px;flex:none" role="img" aria-label="Portrait photo of a team member"></div><div><div class="h">Name Surname</div><div class="t">Position here</div></div></div>
  </div>
  <footer class="foot"><span class="mk"></span><b>MERIDIAN</b><em>Connecting the brightest minds in healthcare</em><i>34</i></footer>
</section>
<section class="slide">
  <div class="s-title">Customer Testimonials</div>
  <div class="a bg-slate" style="left:0;top:95px;width:396px;height:70px"></div>
  <div class="a dot ph" style="left:40px;top:60px;width:50px;height:50px;border:3px solid #fff" role="img" aria-label="Portrait photo of a client"></div>
  <p class="a t w" style="left:110px;top:110px;width:260px">“The hub cut our referral waiting time in half and our staff finally know who to call.”</p>
  <footer class="foot"><span class="mk"></span><b>MERIDIAN</b><em>Connecting the brightest minds in healthcare</em><i>35</i></footer>
</section>

<!-- Row 13 -->
<section class="slide">
  <div class="s-title">Two Pictures Slide</div>
  <div class="a ph" style="left:14px;top:40px;width:180px;height:150px" role="img" aria-label="Photo of a group of doctors"></div>
  <div class="a ph warm" style="left:202px;top:40px;width:180px;height:150px" role="img" aria-label="Photo of two nurses"></div>
  <footer class="foot"><span class="mk"></span><b>MERIDIAN</b><em>Connecting the brightest minds in healthcare</em><i>36</i></footer>
</section>
<section class="slide">
  <div class="s-title">Title And Image + Text</div>
  <div class="a ph teal" style="left:120px;top:40px;width:262px;height:90px" role="img" aria-label="Microscope image of cells"></div>
  <p class="a t" style="left:14px;top:140px;width:368px">Our liaison teams link clinics, labs and regional partners so patients receive faster, clearer and better coordinated care every day.</p>
  <footer class="foot"><span class="mk"></span><b>MERIDIAN</b><em>Connecting the brightest minds in healthcare</em><i>37</i></footer>
</section>
<section class="slide">
  <div class="s-title">Sales Comparison</div>
  <div class="a" style="left:30px;top:50px;width:130px;height:90px;border-bottom:1px solid var(--line)">
    <div class="bar bg-navy" style="left:10px;width:18px;height:50px"></div><div class="bar bg-navy" style="left:40px;width:18px;height:70px"></div><div class="bar bg-navy" style="left:70px;width:18px;height:40px"></div><div class="bar bg-navy" style="left:100px;width:18px;height:80px"></div>
  </div>
  <div class="a dot bg-mist" style="left:183px;top:80px;width:30px;height:30px"></div>
  <div class="a" style="left:236px;top:50px;width:130px;height:90px;border-bottom:1px solid var(--line)">
    <div class="bar bg-blue" style="left:10px;width:18px;height:60px"></div><div class="bar bg-blue" style="left:40px;width:18px;height:45px"></div><div class="bar bg-blue" style="left:70px;width:18px;height:85px"></div><div class="bar bg-blue" style="left:100px;width:18px;height:65px"></div>
  </div>
  <div class="a num" style="left:30px;top:150px;font-size:20px">45%</div>
  <div class="a num" style="left:236px;top:150px;font-size:20px">68%</div>
  <footer class="foot"><span class="mk"></span><b>MERIDIAN</b><em>Connecting the brightest minds in healthcare</em><i>38</i></footer>
</section>

<!-- Row 14 -->
<section class="slide">
  <div class="a ph warm" style="left:0;top:0;width:396px;height:209px" role="img" aria-label="Photo of doctors in a hallway, greyed"></div>
  <div class="a" style="left:14px;top:110px;width:368px;display:grid;grid-template-columns:repeat(3,1fr);gap:6px">
    <div class="bg-navy" style="padding:8px;height:70px"><div class="h w">Heading</div><p class="t w">Short line here.</p></div>
    <div class="bg-navy" style="padding:8px;height:70px"><div class="h w">Heading</div><p class="t w">Short line here.</p></div>
    <div class="bg-blue" style="padding:8px;height:70px"><div class="h w">Heading</div><p class="t w">Short line here.</p></div>
  </div>
  <footer class="foot"><span class="mk"></span><b>MERIDIAN</b><em>Connecting the brightest minds in healthcare</em><i>39</i></footer>
</section>
<section class="slide bg-slate">
  <div class="a brand" style="left:0;right:0;top:70px;justify-content:center;font-size:12px"><span class="c" style="width:16px;height:16px"></span>MERIDIAN LIAISON HUB</div>
  <div class="a" style="left:0;right:0;top:110px;text-align:center;font-family:Montserrat,Arial,sans-serif;font-weight:300;font-size:11px;color:#fff">This is Your Timeline Page</div>
</section>
<section class="slide">
  <div class="s-title">Your Title</div>
  <div class="a bg-navy" style="left:14px;top:110px;width:180px;height:75px;padding:10px"><div class="h w">Heading Here</div><p class="t w">Short summary of this section topic.</p></div>
  <div class="a ph" style="left:200px;top:30px;width:182px;height:155px" role="img" aria-label="Photo of a doctor team"></div>
  <footer class="foot"><span class="mk"></span><b>MERIDIAN</b><em>Connecting the brightest minds in healthcare</em><i>40</i></footer>
</section>

<!-- Row 15 -->
<section class="slide">
  <div class="s-title">Your Title</div>
  <div class="a" style="left:14px;top:45px;width:150px;display:grid;gap:10px">
    <div class="row-item"><span class="ic sq"></span><div class="t">Short note about this item.</div></div>
    <div class="row-item"><span class="ic sq"></span><div class="t">Short note about this item.</div></div>
    <div class="row-item"><span class="ic sq"></span><div class="t">Short note about this item.</div></div>
  </div>
  <div class="a ph" style="left:180px;top:30px;width:202px;height:100px" role="img" aria-label="Photo of a doctor reviewing a tablet"></div>
  <div class="a bg-navy" style="left:180px;top:130px;width:202px;height:60px;padding:8px"><p class="t w">Our liaison teams link clinics and partners so patients receive clearer care.</p></div>
  <footer class="foot"><span class="mk"></span><b>MERIDIAN</b><em>Connecting the brightest minds in healthcare</em><i>41</i></footer>
</section>
<section class="slide">
  <div class="a" style="left:197px;top:15px;width:2px;height:180px;background:var(--line)"></div>
  <div class="a dot bg-navy" style="left:192px;top:45px;width:12px;height:12px"></div>
  <div class="a dot bg-blue" style="left:192px;top:100px;width:12px;height:12px"></div>
  <div class="a dot bg-grey" style="left:192px;top:155px;width:12px;height:12px"></div>
  <div class="a" style="left:80px;top:40px;width:100px;text-align:right"><div class="h">Your Title</div><p class="t">Short line here.</p></div>
  <div class="a" style="left:215px;top:92px"><div class="num" style="font-size:18px">85%</div></div>
  <div class="a" style="left:80px;top:150px;width:100px;text-align:right"><div class="h">Your Title</div><p class="t">Short line here.</p></div>
  <footer class="foot"><span class="mk"></span><b>MERIDIAN</b><em>Connecting the brightest minds in healthcare</em><i>42</i></footer>
</section>
<section class="slide">
  <div class="s-title">Who We Are?</div>
  <div class="a" style="left:14px;top:48px;width:180px;display:grid;gap:12px">
    <div style="border-bottom:1px solid var(--line);padding-bottom:4px"><div class="h b">A Title About Contents</div></div>
    <div style="border-bottom:1px solid var(--line);padding-bottom:4px"><div class="h b">A Title About Contents</div></div>
    <div style="border-bottom:1px solid var(--line);padding-bottom:4px"><div class="h b">A Title About Contents</div></div>
  </div>
  <div class="a ph" style="left:210px;top:30px;width:172px;height:160px" role="img" aria-label="Photo of a smiling doctor"></div>
  <footer class="foot"><span class="mk"></span><b>MERIDIAN</b><em>Connecting the brightest minds in healthcare</em><i>43</i></footer>
</section>

<!-- Row 16 -->
<section class="slide">
  <div class="s-title">Bullet &amp; Chart Area</div>
  <svg class="a" style="left:30px;top:50px" width="120" height="120" viewBox="0 0 120 120"><circle cx="60" cy="60" r="55" fill="#1d4f86"/><path d="M60 60 L60 5 A55 55 0 0 1 112 78 Z" fill="#2a74c9"/><path d="M60 60 L112 78 A55 55 0 0 1 40 111 Z" fill="#6b7075"/></svg>
  <div class="a" style="left:200px;top:55px;width:180px;display:grid;gap:12px">
    <div class="row-item"><span class="ic sq bg-navy"></span><div class="t">Heading text here.</div></div>
    <div class="row-item"><span class="ic sq"></span><div class="t">Heading text here.</div></div>
    <div class="row-item"><span class="ic sq" style="background:var(--grey)"></span><div class="t">Heading text here.</div></div>
  </div>
  <footer class="foot"><span class="mk"></span><b>MERIDIAN</b><em>Connecting the brightest minds in healthcare</em><i>44</i></footer>
</section>
<section class="slide">
  <div class="a" style="left:197px;top:10px;width:2px;height:140px;background:var(--line)"></div>
  <div class="a dot bg-navy" style="left:192px;top:40px;width:12px;height:12px"></div>
  <div class="a dot bg-blue" style="left:192px;top:95px;width:12px;height:12px"></div>
  <div class="a" style="left:215px;top:35px"><div class="h">Your Title Here</div></div>
  <div class="a" style="left:130px;top:90px;width:50px;text-align:right"><div class="num" style="font-size:14px">50%</div></div>
  <div class="a" style="left:0;right:0;top:165px;display:flex;justify-content:center;gap:5px;font-family:Montserrat,Arial,sans-serif;font-weight:700;font-size:11px;color:var(--navy);align-items:center"><span class="dot bg-navy" style="width:14px;height:14px"></span>MERIDIAN</div>
  <footer class="foot"><span class="mk"></span><b>MERIDIAN</b><em>Connecting the brightest minds in healthcare</em><i>45</i></footer>
</section>
<section class="slide">
  <div class="s-title">Bullet &amp; Chart Area</div>
  <div class="a" style="left:14px;top:48px;width:150px;display:grid;gap:12px">
    <div class="row-item"><span class="ic sq"></span><div class="t">Heading text here.</div></div>
    <div class="row-item"><span class="ic sq"></span><div class="t">Heading text here.</div></div>
    <div class="row-item"><span class="ic sq"></span><div class="t">Heading text here.</div></div>
  </div>
  <div class="a" style="left:190px;top:48px;width:190px;display:grid;gap:7px">
    <div class="bg-navy" style="height:9px;width:85%"></div><div class="bg-blue" style="height:9px;width:65%"></div>
    <div class="bg-navy" style="height:9px;width:95%"></div><div class="bg-blue" style="height:9px;width:55%"></div>
    <div class="bg-navy" style="height:9px;width:75%"></div><div class="bg-blue" style="height:9px;width:45%"></div>
    <div class="bg-navy" style="height:9px;width:60%"></div>
  </div>
  <footer class="foot"><span class="mk"></span><b>MERIDIAN</b><em>Connecting the brightest minds in healthcare</em><i>46</i></footer>
</section>

<!-- Row 17 -->
<section class="slide">
  <div class="s-title">Bullet &amp; Chart Area</div>
  <div class="a" style="left:14px;top:45px;width:200px;height:120px;border-bottom:1px solid var(--line)">
    <div class="bar bg-navy" style="left:10px;width:12px;height:70px"></div><div class="bar bg-blue" style="left:24px;width:12px;height:50px"></div>
    <div class="bar bg-navy" style="left:60px;width:12px;height:90px"></div><div class="bar bg-blue" style="left:74px;width:12px;height:60px"></div>
    <div class="bar bg-navy" style="left:110px;width:12px;height:55px"></div><div class="bar bg-blue" style="left:124px;width:12px;height:100px"></div>
    <div class="bar bg-navy" style="left:160px;width:12px;height:80px"></div><div class="bar bg-blue" style="left:174px;width:12px;height:40px"></div>
  </div>
  <div class="a" style="left:235px;top:55px;width:150px;display:grid;gap:12px">
    <div class="row-item"><span class="ic sq bg-navy"></span><div class="t">Heading text here.</div></div>
    <div class="row-item"><span class="ic sq"></span><div class="t">Heading text here.</div></div>
    <div class="row-item"><span class="ic sq" style="background:var(--grey)"></span><div class="t">Heading text here.</div></div>
  </div>
  <footer class="foot"><span class="mk"></span><b>MERIDIAN</b><em>Connecting the brightest minds in healthcare</em><i>47</i></footer>
</section>
<section class="slide">
  <div class="s-title">Column Chart</div>
  <div class="a" style="left:30px;top:40px;width:336px;height:110px;border-bottom:1px solid var(--line)">
    <div class="bar bg-navy" style="left:20px;width:18px;height:60px"></div><div class="bar bg-blue" style="left:40px;width:18px;height:90px"></div><div class="bar bg-grey" style="left:60px;width:18px;height:40px"></div>
    <div class="bar bg-navy" style="left:130px;width:18px;height:75px"></div><div class="bar bg-blue" style="left:150px;width:18px;height:100px"></div><div class="bar bg-grey" style="left:170px;width:18px;height:55px"></div>
    <div class="bar bg-navy" style="left:240px;width:18px;height:50px"></div><div class="bar bg-blue" style="left:260px;width:18px;height:85px"></div><div class="bar bg-grey" style="left:280px;width:18px;height:65px"></div>
  </div>
  <div class="a" style="left:30px;top:158px;width:336px;display:grid;grid-template-columns:repeat(3,1fr);text-align:center"><p class="t">Short label text</p><p class="t">Short label text</p><p class="t">Short label text</p></div>
  <footer class="foot"><span class="mk"></span><b>MERIDIAN</b><em>Connecting the brightest minds in healthcare</em><i>48</i></footer>
</section>
<section class="slide">
  <div class="s-title">Bar Chart</div>
  <div class="a" style="left:14px;top:45px;width:110px"><div class="h">Heading Here</div><p class="t">Short summary of the figures shown.</p></div>
  <div class="a" style="left:140px;top:40px;width:240px;height:140px;display:grid;grid-template-columns:repeat(6,1fr);gap:12px;align-items:end">
    <div style="height:100%;background:var(--mist);border-radius:8px;position:relative"><div class="bg-navy" style="position:absolute;bottom:0;left:0;right:0;height:60%;border-radius:8px"></div></div>
    <div style="height:100%;background:var(--mist);border-radius:8px;position:relative"><div class="bg-grey" style="position:absolute;bottom:0;left:0;right:0;height:80%;border-radius:8px"></div></div>
    <div style="height:100%;background:var(--mist);border-radius:8px;position:relative"><div class="bg-navy" style="position:absolute;bottom:0;left:0;right:0;height:45%;border-radius:8px"></div></div>
    <div style="height:100%;background:var(--mist);border-radius:8px;position:relative"><div class="bg-grey" style="position:absolute;bottom:0;left:0;right:0;height:70%;border-radius:8px"></div></div>
    <div style="height:100%;background:var(--mist);border-radius:8px;position:relative"><div class="bg-navy" style="position:absolute;bottom:0;left:0;right:0;height:90%;border-radius:8px"></div></div>
    <div style="height:100%;background:var(--mist);border-radius:8px;position:relative"><div class="bg-grey" style="position:absolute;bottom:0;left:0;right:0;height:55%;border-radius:8px"></div></div>
  </div>
  <footer class="foot"><span class="mk"></span><b>MERIDIAN</b><em>Connecting the brightest minds in healthcare</em><i>49</i></footer>
</section>

<!-- Row 18 -->
<section class="slide">
  <div class="s-title">Comparison Gender</div>
  <div class="a" style="left:30px;top:45px;width:336px;display:grid;gap:6px">
    <div style="display:grid;grid-template-columns:40px 1fr 1fr;gap:3px;align-items:center"><span class="t">2014</span><span class="bg-grey" style="height:9px"></span><span class="bg-navy" style="height:9px;width:70%"></span></div>
    <div style="display:grid;grid-template-columns:40px 1fr 1fr;gap:3px;align-items:center"><span class="t">2015</span><span class="bg-grey" style="height:9px;width:80%;justify-self:end"></span><span class="bg-navy" style="height:9px;width:85%"></span></div>
    <div style="display:grid;grid-template-columns:40px 1fr 1fr;gap:3px;align-items:center"><span class="t">2016</span><span class="bg-grey" style="height:9px;width:60%;justify-self:end"></span><span class="bg-navy" style="height:9px;width:90%"></span></div>
    <div style="display:grid;grid-template-columns:40px 1fr 1fr;gap:3px;align-items:center"><span class="t">2017</span><span class="bg-grey" style="height:9px;width:90%;justify-self:end"></span><span class="bg-navy" style="height:9px;width:60%"></span></div>
    <div style="display:grid;grid-template-columns:40px 1fr 1fr;gap:3px;align-items:center"><span class="t">2018</span><span class="bg-grey" style="height:9px;width:70%;justify-self:end"></span><span class="bg-navy" style="height:9px;width:75%"></span></div>
    <div style="display:grid;grid-template-columns:40px 1fr 1fr;gap:3px;align-items:center"><span class="t">2019</span><span class="bg-grey" style="height:9px;width:85%;justify-self:end"></span><span class="bg-navy" style="height:9px;width:80%"></span></div>
  </div>
  <footer class="foot"><span class="mk"></span><b>MERIDIAN</b><em>Connecting the brightest minds in healthcare</em><i>50</i></footer>
</section>
<section class="slide">
  <div class="s-title">Arrow Diagram</div>
  <svg class="a" style="left:20px;top:40px" width="356" height="150" viewBox="0 0 356 150">
    <polygon points="10,75 60,25 110,75 60,125" fill="#1d4f86"/>
    <polygon points="95,75 145,25 195,75 145,125" fill="#2a74c9"/>
    <polygon points="180,75 230,25 280,75 230,125" fill="#6b7075"/>
    <polygon points="265,75 315,25 356,75 315,125" fill="#1d4f86"/>
    <path d="M60 20 L300 20 L300 8 L330 22 L300 36" fill="none" stroke="#2a74c9" stroke-width="3"/>
    <text x="60" y="78" text-anchor="middle" font-family="Montserrat" font-size="7" fill="#fff">Step 01</text>
    <text x="145" y="78" text-anchor="middle" font-family="Montserrat" font-size="7" fill="#fff">Step 02</text>
    <text x="230" y="78" text-anchor="middle" font-family="Montserrat" font-size="7" fill="#fff">Step 03</text>
    <text x="315" y="78" text-anchor="middle" font-family="Montserrat" font-size="7" fill="#fff">Step 04</text>
  </svg>
  <footer class="foot"><span class="mk"></span><b>MERIDIAN</b><em>Connecting the brightest minds in healthcare</em><i>51</i></footer>
</section>
<section class="slide">
  <div class="s-title">Investment Infographic</div>
  <div class="a num" style="left:20px;top:48px;font-size:26px">75%</div>
  <div class="a" style="left:110px;top:56px;width:150px;display:grid;grid-template-columns:repeat(10,1fr);gap:2px"><span class="bg-navy" style="height:12px"></span><span class="bg-navy" style="height:12px"></span><span class="bg-navy" style="height:12px"></span><span class="bg-navy" style="height:12px"></span><span class="bg-navy" style="height:12px"></span><span class="bg-navy" style="height:12px"></span><span class="bg-navy" style="height:12px"></span><span class="bg-navy" style="height:12px"></span><span class="bg-mist" style="height:12px"></span><span class="bg-mist" style="height:12px"></span></div>
  <div class="a num" style="left:280px;top:50px;font-size:18px;color:var(--grey)">2017</div>
  <div class="a num" style="left:20px;top:110px;font-size:26px">80%</div>
  <div class="a" style="left:110px;top:118px;width:150px;display:grid;grid-template-columns:repeat(10,1fr);gap:2px"><span class="bg-blue" style="height:12px"></span><span class="bg-blue" style="height:12px"></span><span class="bg-blue" style="height:12px"></span><span class="bg-blue" style="height:12px"></span><span class="bg-blue" style="height:12px"></span><span class="bg-blue" style="height:12px"></span><span class="bg-blue" style="height:12px"></span><span class="bg-blue" style="height:12px"></span><span class="bg-mist" style="height:12px"></span><span class="bg-mist" style="height:12px"></span></div>
  <div class="a num" style="left:280px;top:112px;font-size:18px;color:var(--grey)">2018</div>
  <footer class="foot"><span class="mk"></span><b>MERIDIAN</b><em>Connecting the brightest minds in healthcare</em><i>52</i></footer>
</section>

<!-- Row 19 -->
<section class="slide">
  <div class="s-title">Money Bag Infographic</div>
  <div class="a" style="left:20px;top:45px;width:100px"><div class="h">Your Title Goes Here</div><p class="t">Short note on funding split.</p></div>
  <div class="a" style="left:135px;top:50px;width:110px;height:135px;background:linear-gradient(160deg,#6b7075,#3a3d41)" role="img" aria-label="Illustration of a money bag"></div>
  <div class="a" style="left:255px;top:60px;display:grid;gap:18px">
    <div style="display:flex;gap:6px;align-items:center"><span class="bg-navy" style="width:40px;height:2px"></span><span class="num" style="font-size:14px">12%</span></div>
    <div style="display:flex;gap:6px;align-items:center"><span class="bg-navy" style="width:40px;height:2px"></span><span class="num" style="font-size:14px">32%</span></div>
    <div style="display:flex;gap:6px;align-items:center"><span class="bg-navy" style="width:40px;height:2px"></span><span class="num" style="font-size:14px">-23%</span></div>
  </div>
  <footer class="foot"><span class="mk"></span><b>MERIDIAN</b><em>Connecting the brightest minds in healthcare</em><i>53</i></footer>
</section>
<section class="slide">
  <div class="s-title">Shopping Bag Infographic</div>
  <div class="a" style="left:30px;top:40px;width:190px;height:140px;border-bottom:1px solid var(--line)">
    <div class="bar bg-grey" style="left:10px;width:45px;height:60px"></div><div class="a num" style="left:14px;bottom:65px;font-size:10px">$100</div>
    <div class="bar bg-slate" style="left:70px;width:45px;height:85px"></div><div class="a num" style="left:74px;bottom:90px;font-size:10px">$199</div>
    <div class="bar bg-blue" style="left:130px;width:45px;height:110px"></div><div class="a num" style="left:134px;bottom:115px;font-size:10px">$299</div>
  </div>
  <div class="a" style="left:240px;top:50px;width:140px;display:grid;gap:12px">
    <div class="row-item"><span class="ic"></span><div class="t">Short line of text here.</div></div>
    <div class="row-item"><span class="ic"></span><div class="t">Short line of text here.</div></div>
    <div class="row-item"><span class="ic"></span><div class="t">Short line of text here.</div></div>
  </div>
  <footer class="foot"><span class="mk"></span><b>MERIDIAN</b><em>Connecting the brightest minds in healthcare</em><i>54</i></footer>
</section>
<section class="slide">
  <div class="s-title">Basic Chevron Process</div>
  <svg class="a" style="left:14px;top:75px" width="368" height="40" viewBox="0 0 368 40">
    <polygon points="0,0 85,0 100,20 85,40 0,40" fill="#1d4f86"/>
    <polygon points="90,0 175,0 190,20 175,40 90,40 105,20" fill="#2a74c9"/>
    <polygon points="180,0 265,0 280,20 265,40 180,40 195,20" fill="#1d4f86"/>
    <polygon points="270,0 353,0 368,20 353,40 270,40 285,20" fill="#2a74c9"/>
  </svg>
  <div class="a" style="left:14px;top:125px;width:368px;display:grid;grid-template-columns:repeat(4,1fr);gap:6px">
    <p class="t">Intake and triage step.</p><p class="t">Specialist match step.</p><p class="t">Booking and transfer.</p><p class="t">Follow up and report.</p>
  </div>
  <footer class="foot"><span class="mk"></span><b>MERIDIAN</b><em>Connecting the brightest minds in healthcare</em><i>55</i></footer>
</section>

<!-- Row 20 -->
<section class="slide">
  <div class="s-title">Pestel Analysis</div>
  <svg class="a" style="left:30px;top:55px" width="336" height="110" viewBox="0 0 336 110">
    <g font-family="Montserrat" font-size="14" fill="#fff" text-anchor="middle">
      <polygon points="28,10 56,26 56,58 28,74 0,58 0,26" fill="#1d4f86"/><text x="28" y="47">P</text>
      <polygon points="84,36 112,52 112,84 84,100 56,84 56,52" fill="#2a74c9"/><text x="84" y="73">E</text>
      <polygon points="140,10 168,26 168,58 140,74 112,58 112,26" fill="#1d4f86"/><text x="140" y="47">S</text>
      <polygon points="196,36 224,52 224,84 196,100 168,84 168,52" fill="#2a74c9"/><text x="196" y="73">T</text>
      <polygon points="252,10 280,26 280,58 252,74 224,58 224,26" fill="#1d4f86"/><text x="252" y="47">E</text>
      <polygon points="308,36 336,52 336,84 308,100 280,84 280,52" fill="#2a74c9"/><text x="308" y="73">L</text>
    </g>
  </svg>
  <footer class="foot"><span class="mk"></span><b>MERIDIAN</b><em>Connecting the brightest minds in healthcare</em><i>56</i></footer>
</section>
<section class="slide">
  <div class="s-title">Three Steps</div>
  <div class="a" style="left:14px;top:50px;width:170px;display:grid;gap:12px">
    <div class="row-item"><span class="ic"></span><div class="t">Step one short line.</div></div>
    <div class="row-item"><span class="ic"></span><div class="t">Step two short line.</div></div>
    <div class="row-item"><span class="ic"></span><div class="t">Step three short line.</div></div>
  </div>
  <svg class="a" style="left:230px;top:35px" width="140" height="160" viewBox="0 0 140 160">
    <circle cx="85" cy="35" r="26" fill="none" stroke="#1d4f86" stroke-width="12"/>
    <circle cx="55" cy="80" r="26" fill="none" stroke="#6b7075" stroke-width="12"/>
    <circle cx="85" cy="125" r="26" fill="none" stroke="#2a74c9" stroke-width="12"/>
  </svg>
  <footer class="foot"><span class="mk"></span><b>MERIDIAN</b><em>Connecting the brightest minds in healthcare</em><i>57</i></footer>
</section>
<section class="slide">
  <div class="s-title">Project Timeline</div>
  <div class="a" style="left:14px;top:42px;width:368px;height:150px;display:grid;grid-template-columns:70px repeat(6,1fr);grid-auto-rows:18px;font-size:5px;color:var(--grey)">
    <span></span><span class="bg-slate" style="color:#fff;padding:4px">Jan</span><span class="bg-slate" style="color:#fff;padding:4px">Feb</span><span class="bg-slate" style="color:#fff;padding:4px">Mar</span><span class="bg-slate" style="color:#fff;padding:4px">Apr</span><span class="bg-slate" style="color:#fff;padding:4px">May</span><span class="bg-slate" style="color:#fff;padding:4px">Jun</span>
    <span style="padding:4px">Planning</span><span class="bg-navy" style="grid-column:span 2;margin:4px 0"></span><span style="grid-column:span 4"></span>
    <span style="padding:4px">Research</span><span></span><span class="bg-blue" style="grid-column:span 2;margin:4px 0"></span><span style="grid-column:span 3"></span>
    <span style="padding:4px">Design</span><span style="grid-column:span 2"></span><span class="bg-navy" style="grid-column:span 2;margin:4px 0"></span><span style="grid-column:span 2"></span>
    <span style="padding:4px">Pilot</span><span style="grid-column:span 3"></span><span class="bg-blue" style="grid-column:span 2;margin:4px 0"></span><span></span>
    <span style="padding:4px">Launch</span><span style="grid-column:span 4"></span><span class="bg-navy" style="grid-column:span 2;margin:4px 0"></span>
  </div>
  <footer class="foot"><span class="mk"></span><b>MERIDIAN</b><em>Connecting the brightest minds in healthcare</em><i>58</i></footer>
</section>

<!-- Row 21 -->
<section class="slide" style="grid-column:1/2;margin-left:100px;width:396px">
  <div class="s-title">Three Bullets Area</div>
  <div class="a ph" style="left:14px;top:40px;width:368px;height:150px" role="img" aria-label="Photo of three smiling doctors"></div>
  <div class="a" style="left:90px;top:150px;display:flex;gap:70px"><span class="dot bg-navy" style="width:28px;height:28px;border:3px solid #fff"></span><span class="dot bg-blue" style="width:28px;height:28px;border:3px solid #fff"></span><span class="dot bg-navy" style="width:28px;height:28px;border:3px solid #fff"></span></div>
  <footer class="foot"><span class="mk"></span><b>MERIDIAN</b><em>Connecting the brightest minds in healthcare</em><i>59</i></footer>
</section>
<section class="slide" style="grid-column:2/3;margin-left:100px;width:396px">
  <div class="a ph dark" style="inset:0" role="img" aria-label="Dark photo of a smiling doctor"></div>
  <div class="a" style="inset:0;background:rgba(50,54,58,.6)"></div>
  <div class="a big" style="left:20px;top:70px;font-size:22px">THANK YOU</div>
  <div class="a t w" style="left:20px;top:104px;display:grid;gap:4px">
    <span>Meridian Liaison Hub</span>
    <span>www.meridianliaisonhub.example</span>
    <span>Connecting the brightest minds in healthcare</span>
  </div>
</section>

</main>
</body>
</html>
```